Web Design Project for starting CCTV/Camera security installer/reseller

Hello,

An old class mate is starting his own little CCTV/Camera security business as a one-man-gang.

He asked me to do his website but unfortunatly my design skills are not worth looking at :) The coding is no problem.

So I'm here to request a design.

What he wants is a site that lists the products he might install which is based on a small tree structure. So see it as a shop overview/display but without the baskets & cashout options.

you can find a site structure scheme, logo, product images & data sheet pdf's at this filvaultra address:

https://www.filvaultra.com/sh/kq7zt3908wx4pl2/vnRtLoBe5y/Lumo-Ward

the site itself is http://www.lumo-ward.be but only has a splash screen until I have a design for it.

the logo is a bit out of proportions, not sure if you can make something good out of it :/

Most content is in Dutch, I'll see if I can translate the needed parts...
Updates

Dear designers,

I have some good new for you.

You are allowed to use only that chrome Lumo-Ward part of the logo,
which should make things a lot easier to fit into your design ideas.

Keep up the creativity!

Dear designers,

I uploaded a new logo to the filvaultra space.

It's a png but unfortunately it's not transparent, I'm still waiting for that one
but you know how to erase it in photoshop.

Target Market(s)

people looking for a visual solution to protect their company/home

Industry/Entity Type

Security

Requirements
Must have
• an iconized way to browse/display a tree. (not the traditional folder/explorer style)

maybe first a page with buttons/icons showing level 1 the group types (IP cams, IP servers, Accessories)

level 2 product groups (dome cam, ptz cam etc)

level 3 the actual product + a link to a pdf datasheet (if any)

could be multipage or maybe in/on-page since the product list won't be that huge.

maybe some random product info left and/or right so that the content area is not massive since he has not much to type
;)

```html
<!DOCTYPE html>
<html lang="en">
<head>
<meta charset="utf-8">
<title>Lumo-Ward</title>
<link rel="stylesheet" href="https://fonts.googleapis.com/css2?family=Open+Sans:wght@400;600;700&family=Noto+Serif:wght@400;700&display=swap">
<style>
:root{
  --dark:#151515;
  --dark-2:#222;
  --red:#d7262b;
  --red-dark:#a81b1f;
  --text:#555;
  --muted:#888;
  --line:#dcdcdc;
  --panel:#f4f4f4;
  --white:#fff;
}
*{box-sizing:border-box;margin:0;padding:0}
html,body{width:774px;height:1200px;overflow:hidden}
body{position:relative;background:var(--white);font-family:"Open Sans",Arial,sans-serif;color:var(--text);font-size:9px}
.topbar{position:absolute;left:0;top:0;width:774px;height:34px;background:linear-gradient(#2a2a2a,var(--dark))}
.brand{position:absolute;left:77px;top:0;width:117px;height:74px;background:linear-gradient(#fafafa,#d9d9d9);border:1px solid #bbb;border-top:0;display:flex;align-items:center;justify-content:center;gap:6px;z-index:3;box-shadow:0 2px 6px rgba(0,0,0,.3)}
.brand-mark{width:10px;height:10px;background:var(--red)}
.brand-name{font-weight:700;font-size:14px;color:#333}
.nav{position:absolute;left:278px;top:0;display:flex;height:34px;align-items:center}
.nav a{color:#ccc;text-decoration:none;font-size:9px;font-weight:600;padding:0 12px;line-height:34px}
.nav a.active{background:#444;color:var(--white)}
.call{position:absolute;left:516px;top:0;width:175px;height:31px;background:var(--red);color:var(--white);font-weight:700;font-size:12px;display:flex;align-items:center;justify-content:center}
.hero{position:absolute;left:0;top:34px;width:774px;height:286px;background:radial-gradient(ellipse at 60% 40%,#fbfbfb,#d5d5d5 80%)}
.hero h1{position:absolute;left:120px;top:62px;font-family:"Noto Serif",Georgia,serif;font-size:25px;color:#333;font-weight:700}
.hero ul{position:absolute;left:120px;top:104px;list-style:none}
.hero li{font-size:10px;color:#555;line-height:20px;display:flex;align-items:center;gap:7px}
.tick{width:9px;height:9px}
.hero-img{position:absolute;left:426px;top:24px;width:220px;height:226px;background:linear-gradient(#5b6066,#1e2226);border-radius:3px}
.dots{position:absolute;left:120px;top:270px;display:flex;gap:6px}
.dots span{width:7px;height:7px;border-radius:50%;background:#bbb}
.dots span:first-child{background:#777}
.cards{position:absolute;left:85px;top:360px;display:flex;gap:18px}
.card{width:190px;height:220px;border:1px solid var(--line);background:var(--white);box-shadow:0 1px 3px rgba(0,0,0,.1);padding:10px 10px}
.card h3{font-size:12px;font-weight:700;color:#333;border-bottom:1px solid var(--line);padding-bottom:6px}
.card h3 em{font-style:normal;color:var(--red)}
.card-img{height:95px;margin:10px 0;background:linear-gradient(#f4f4f4,#cfcfcf)}
.card p{font-size:7px;line-height:10px;color:var(--muted)}
.more{float:right;margin-top:8px;background:var(--red);color:var(--white);font-size:7px;font-weight:700;padding:3px 7px;border-radius:2px}
.welcome{position:absolute;left:85px;top:612px;width:430px}
.section-title{font-size:11px;font-weight:700;color:#333;text-transform:uppercase;border-bottom:1px solid var(--line);padding-bottom:5px}
.section-title em{font-style:normal;color:var(--red)}
.faq{list-style:none;margin-top:8px}
.faq li{background:var(--panel);border:1px solid #e6e6e6;font-size:7.5px;font-style:italic;color:#666;padding:5px 8px;margin-bottom:5px}
.welcome p{font-size:7.5px;line-height:11px;color:var(--muted);margin-top:6px}
.install{position:absolute;left:540px;top:612px;width:151px}
.install-img{margin-top:8px;height:112px;background:linear-gradient(#8fb0cc,#3f6283)}
.footer{position:absolute;left:0;top:818px;width:774px;height:356px;background:var(--dark)}
.footer h2{position:absolute;left:85px;top:18px;color:var(--red);font-size:12px;font-weight:700}
.address{position:absolute;left:85px;top:48px;color:#bbb;font-size:7.5px;line-height:11px;list-style:none}
.address li{display:flex;gap:6px;align-items:flex-start;margin-bottom:4px}
.address svg{flex:none;margin-top:1px}
.phone-big{position:absolute;left:540px;top:14px;color:var(--white);font-size:17px;font-weight:600;display:flex;gap:8px;align-items:center}
.map{position:absolute;left:335px;top:64px;width:356px;height:212px;background:linear-gradient(135deg,#ececec,#d6d6cf)}
.form{position:absolute;left:85px;top:150px;width:237px}
.field{background:#2e2e2e;border:1px solid #3c3c3c;color:#999;font-size:7px;padding:4px 6px;height:22px;margin-bottom:6px}
.field.area{height:60px}
.send{display:inline-block;margin-top:8px;background:var(--red);color:var(--white);font-weight:700;font-size:8px;padding:5px 12px}
.bottombar{position:absolute;left:0;top:1174px;width:774px;height:26px;background:var(--dark-2);border-top:1px solid #333}
.bottombar p{position:absolute;left:85px;top:8px;font-size:7px;color:#888}
.social{position:absolute;left:644px;top:6px;display:flex;gap:5px}
.social span{width:13px;height:13px;border-radius:50%;background:#666}
</style>
</head>
<body>
<header class="topbar">
  <div class="brand"><span class="brand-mark"></span><span class="brand-name">Lumo-Ward</span></div>
  <nav class="nav"><a class="active">HOME</a><a>TIPS</a><a>INSTALLATION</a><a>CONTACT</a></nav>
  <div class="call">Call Us +32 470 55 21 08</div>
</header>

<section class="hero">
  <h1>Lumo - Ward</h1>
  <ul>
    <li><svg class="tick" viewBox="0 0 10 10"><path d="M1 5l3 3 5-7" fill="none" stroke="#d7262b" stroke-width="2"/></svg>Secure your home with smart camera views.</li>
    <li><svg class="tick" viewBox="0 0 10 10"><path d="M1 5l3 3 5-7" fill="none" stroke="#d7262b" stroke-width="2"/></svg>Clear images by day and by night.</li>
    <li><svg class="tick" viewBox="0 0 10 10"><path d="M1 5l3 3 5-7" fill="none" stroke="#d7262b" stroke-width="2"/></svg>Remote access from any phone or laptop.</li>
    <li><svg class="tick" viewBox="0 0 10 10"><path d="M1 5l3 3 5-7" fill="none" stroke="#d7262b" stroke-width="2"/></svg>Reliable storage on compact servers.</li>
    <li><svg class="tick" viewBox="0 0 10 10"><path d="M1 5l3 3 5-7" fill="none" stroke="#d7262b" stroke-width="2"/></svg>Personal advice and local installation.</li>
    <li><svg class="tick" viewBox="0 0 10 10"><path d="M1 5l3 3 5-7" fill="none" stroke="#d7262b" stroke-width="2"/></svg>Fair prices with no hidden costs.</li>
  </ul>
  <div class="hero-img" role="img" aria-label="Server racks with network video recorders"></div>
  <div class="dots"><span></span><span></span><span></span></div>
</section>

<section class="cards">
  <article class="card">
    <h3><em>IP</em> CAMS</h3>
    <div class="card-img" role="img" aria-label="Dome and bullet IP cameras"></div>
    <p>Dome, bullet and PTZ cameras for indoor and outdoor use, with sharp images and easy network setup for every type of property.</p>
    <span class="more">Read More ›</span>
  </article>
  <article class="card">
    <h3><em>IP</em> SERVERS</h3>
    <div class="card-img" role="img" aria-label="Network video recorder servers"></div>
    <p>Compact recorders and servers that store your footage safely and let you review every event quickly from one clear overview.</p>
    <span class="more">Read More ›</span>
  </article>
  <article class="card">
    <h3><em>IP</em> ACCESSORIES</h3>
    <div class="card-img" role="img" aria-label="Camera mounts and cabling accessories"></div>
    <p>Mounts, cables, switches and power units that complete your setup and keep every camera running without any interruption.</p>
    <span class="more">Read More ›</span>
  </article>
</section>

<section class="welcome">
  <h2 class="section-title">Welcome at <em>Lumo Ward camera surveillance</em></h2>
  <ul class="faq">
    <li>Are you looking for a camera system for your home or company?</li>
    <li>Then you are at Lumo Ward at the right address!</li>
    <li>We offer a large amount of surveillance cameras, video storage systems and accessories.</li>
  </ul>
  <p>We also install complete systems for private and business clients, including cables and power, so you do not have to worry about anything.</p>
</section>

<aside class="install">
  <h2 class="section-title">Installation <em>Service</em></h2>
  <div class="install-img" role="img" aria-label="Technician installing a security camera"></div>
</aside>

<footer class="footer">
  <h2>CONTACT</h2>
  <ul class="address">
    <li><svg width="8" height="10" viewBox="0 0 8 10"><path d="M4 0a3.5 3.5 0 0 0-3.5 3.5C.5 6 4 10 4 10s3.5-4 3.5-6.5A3.5 3.5 0 0 0 4 0z" fill="#fff"/></svg><span>Lumo Ward Beveiliging<br>Veldlaan 14<br>9000 Gent<br>België</span></li>
    <li><svg width="8" height="8" viewBox="0 0 8 8"><rect x="0" y="1" width="8" height="6" fill="#fff"/></svg><span>info@lumo-ward.be</span></li>
    <li><svg width="8" height="8" viewBox="0 0 8 8"><circle cx="4" cy="4" r="3.5" fill="#fff"/></svg><span>+32 470 55 21 08</span></li>
  </ul>
  <div class="phone-big"><svg width="16" height="16" viewBox="0 0 16 16"><path d="M3 1l3 3-2 2c1 2 3 4 5 5l2-2 3 3-2 3C7 15 1 9 0 3z" fill="#fff"/></svg>+32 470 55 21 08</div>
  <div class="map" role="img" aria-label="Street map with the office location"></div>
  <form class="form">
    <div class="field">Name</div>
    <div class="field">E-mail</div>
    <div class="field">Subject</div>
    <div class="field area">Questions &amp; Remarks</div>
    <span class="send">SEND</span>
  </form>
</footer>
<div class="bottombar">
  <p>Copyright © 2013 Lumo-Ward. All Rights Reserved.</p>
  <div class="social"><span></span><span></span><span></span></div>
</div>
</body>
</html>
```